Business Card Design for a Personal Trainer

I need a business card design for my job as a personal trainer. It should have a unique, modern and exclusive design. On the front there should be only my logo with my name and my job. 0163/2918374 Tobias Kellinger Lindenfeldweg 14 80412 Munich Germany The most important contact information is the web adress. it can be bigger than the rest, but its not necessary. The card should be 8,5cmx5,5cm big. Font: Roboto. Colors: black, white, gray, 56c1ff.

```html
<!DOCTYPE html>
<html lang="de">
<head>
<meta charset="utf-8">
<title>Tobias Kellinger – Business Card</title>
<link href="https://fonts.googleapis.com/css2?family=Roboto:wght@300;400;500;700&display=swap" rel="stylesheet">
<style>
  :root {
    --page: #eeeeee;
    --white: #ffffff;
    --wave-light: #7a7a7a;
    --wave-mid: #5d5d5d;
    --wave-dark: #454545;
    --ink: #3a3a3a;
    --ink-soft: #6a6a6a;
    --photo-a: #d9d9d9;
    --photo-b: #8a8a8a;
  }
  * { margin: 0; padding: 0; box-sizing: border-box; }
  html, body {
    width: 1136px; height: 1200px; overflow: hidden;
    background: var(--page);
    font-family: 'Roboto', sans-serif;
  }
  .sheet {
    position: relative; width: 1136px; height: 1200px;
    display: flex; align-items: center; justify-content: center; gap: 40px;
  }
  .card {
    position: relative; width: 520px; height: 336px;
    background: var(--white); overflow: hidden;
    box-shadow: 0 4px 14px rgba(0,0,0,0.35);
  }
  .card-waves { position: absolute; inset: 0; width: 100%; height: 100%; }
  .portrait {
    position: absolute; left: 292px; top: 35px; width: 128px; height: 128px;
    border-radius: 50%;
    background: radial-gradient(circle at 50% 40%, var(--photo-a), var(--photo-b));
    border: 3px solid var(--white);
  }
  .contact-list {
    position: absolute; left: 30px; top: 168px; list-style: none;
    color: var(--white); font-size: 18px; font-weight: 300; letter-spacing: 0.8px;
  }
  .contact-list li { display: flex; align-items: flex-start; height: 26px; }
  .contact-list li.address { height: auto; line-height: 23px; }
  .contact-list .icon { width: 16px; height: 16px; margin: 4px 14px 0 0; flex: none; fill: var(--white); }
  .contact-list .web { font-weight: 700; }
  .title-block {
    position: absolute; right: 36px; top: 44px; text-align: right;
  }
  .title-name { font-size: 20px; font-weight: 700; color: var(--ink); letter-spacing: 0.6px; }
  .title-role { font-size: 15px; font-weight: 400; color: var(--ink-soft); letter-spacing: 0.6px; margin-top: 2px; }
  .brand {
    position: absolute; left: 0; right: 0; top: 232px;
    display: flex; align-items: center; justify-content: center; gap: 12px;
    color: var(--white); font-size: 28px; font-weight: 400; letter-spacing: 0.5px;
  }
  .brand-square { width: 18px; height: 18px; background: var(--white); }
</style>
</head>
<body>
<main class="sheet">

  <section class="card card-back">
    <svg class="card-waves" viewBox="0 0 520 336" preserveAspectRatio="none" aria-hidden="true">
      <path d="M0,58 C110,38 200,62 280,100 C360,138 440,44 520,22 L520,336 L0,336Z" fill="var(--wave-light)"/>
      <path d="M0,76 C110,56 200,82 280,120 C360,156 440,64 520,44 L520,336 L0,336Z" fill="var(--wave-mid)"/>
      <path d="M0,96 C110,78 200,104 280,142 C360,178 440,86 520,66 L520,336 L0,336Z" fill="var(--wave-dark)"/>
    </svg>
    <div class="portrait" role="img" aria-label="Portrait photo of the trainer"></div>
    <ul class="contact-list">
      <li>
        <svg class="icon" viewBox="0 0 16 16"><path d="M3.5 1 L6 3.8 L4.8 5.6 C5.6 7.6 8.4 10.4 10.4 11.2 L12.2 10 L15 12.5 L13 15 C7 14.5 1.5 9 1 3Z"/></svg>
        <span>0163/2918374</span>
      </li>
      <li>
        <svg class="icon" viewBox="0 0 16 16"><path d="M1 3 H15 V13 H1Z M2 4 L8 9 L14 4" fill="var(--white)" stroke="var(--wave-dark)" stroke-width="1.2"/></svg>
        <span>t.kellinger@mailpost.de</span>
      </li>
      <li>
        <svg class="icon" viewBox="0 0 16 16"><circle cx="8" cy="8" r="7"/><path d="M1 8 H15 M8 1 C4 5 4 11 8 15 M8 1 C12 5 12 11 8 15" fill="none" stroke="var(--wave-dark)" stroke-width="1.1"/></svg>
        <span class="web">www.tobiaskellinger.de</span>
      </li>
      <li class="address">
        <svg class="icon" viewBox="0 0 16 16"><path d="M8 0.5 C4.5 0.5 2.5 3 2.5 6 C2.5 10 8 15.5 8 15.5 C8 15.5 13.5 10 13.5 6 C13.5 3 11.5 0.5 8 0.5Z"/><circle cx="8" cy="6" r="2" fill="var(--wave-dark)"/></svg>
        <span>Lindenfeldweg 14<br>80412 München</span>
      </li>
    </ul>
  </section>

  <section class="card card-front">
    <svg class="card-waves" viewBox="0 0 520 336" preserveAspectRatio="none" aria-hidden="true">
      <path d="M0,44 C90,18 170,24 260,62 C350,100 440,118 520,82 L520,336 L0,336Z" fill="var(--wave-light)"/>
      <path d="M0,60 C90,34 170,40 260,80 C350,118 440,136 520,100 L520,336 L0,336Z" fill="var(--wave-mid)"/>
      <path d="M0,78 C90,54 170,60 260,100 C350,138 440,156 520,120 L520,336 L0,336Z" fill="var(--wave-dark)"/>
    </svg>
    <div class="title-block">
      <p class="title-name">Tobias Kellinger</p>
      <p class="title-role">Personal Trainer</p>
    </div>
    <div class="brand">
      <span class="brand-square"></span>
      <span>TOBIAS KELLINGER</span>
    </div>
  </section>

</main>
</body>
</html>
```